GLX Comedy Show needs a Poster Design

"Cousins Weekend Away!" (www.cousinsweekendawaylaughs.example) is a theatre based comedy show about parenting and family. We need to update our marketing materials for the next season. We need an eye-catching, clever poster to help market and sell the show. It should be funny with bright colors.
Updates

Quick update - we have added a few posters with designs that we like.  We also added last year's poster template with the little kid screaming at the top.  

  Please note - Even though we have attached files of posters that we like, we are ALWAYS open to other graphic ideas.  The poster will be used in Theatres and Performing Arts Centers throughout the country.

With regard to size - we will be using the design on different sizes of posters.  If you could provide your designs in 8.5 x 11 form for now, that would be great.  If you have already submitted in another size, that's ok (no need to revise at this point).  Thanks!

Reason: Hi, we are extending the deadline by 3 days to allow time for the producer and director to return from weekend shows to make the final decision. We appreciate all of the entries and are very impressed with the quality of each poster design. Thanks to you all for submitting.

We would like to thank all of the designers who submitted for this project.  We had some really good submissions to choose from.  We wish you all the best with your endeavors.

Target Market(s)

Parents and married couples ages 30-70

Industry/Entity Type

Marketing

Requirements
Must have
• 1) Title of show: Cousins Weekend Away!

2) The poster must convey that this is a comedy show about parenting and family. You can use a tagline or graphics.
possible taglines - Joyfully Always Giggling, Comedy for Grownups, Comedy About Family, etc.

3) Performer names - Linda Pruett & Ray Dunsworth
Nice to have
• Performer headshots, but only if they compliment the design. We would rather see a really funny, clean design that sells the show with funny photos or graphics. If the headshots work with the overall design, that's great. If not, text of the performers names is ok.
Should not have
• no typical comedy icons, i.e., microphone, stage, spotlight
baby items like bottles and diapers might be included, but our show is not just for young parents; it's for parents of all ages.

```html
<!DOCTYPE html>
<html lang="en">
<head>
<meta charset="utf-8">
<title>Cousins Weekend Away! — Poster</title>
<link rel="stylesheet" href="https://fonts.googleapis.com/css2?family=Josefin+Sans:wght@300;400&family=Quicksand:wght@500&display=swap">
<style>
  :root {
    --mint: #12ea8f;
    --white: #ffffff;
    --sky: #1ea7e1;
    --photo-light: #f1f1f1;
    --skin: #e7c3a8;
    --skin-deep: #c98f6c;
  }
  * { box-sizing: border-box; margin: 0; padding: 0; }
  html, body { width: 927px; height: 1200px; overflow: hidden; }
  body { background: var(--mint); }
  .poster {
    position: relative;
    width: 927px;
    height: 1200px;
    background: var(--mint);
    color: var(--white);
    font-family: "Josefin Sans", sans-serif;
    font-weight: 300;
  }
  .connectors { position: absolute; inset: 0; }
  .box { position: absolute; border: 2px solid var(--white); }
  .heading {
    left: 309px; top: 111px; width: 302px; height: 39px;
    display: flex; align-items: center; justify-content: center;
    font-size: 30px; letter-spacing: 5px; padding-top: 4px;
  }
  .performer-name {
    top: 224px; width: 176px; height: 34px;
    display: flex; align-items: center; justify-content: center;
    font-family: "Quicksand", sans-serif; font-weight: 500;
    font-size: 18px; letter-spacing: 1px;
  }
  .performer-name.left { left: 103px; }
  .performer-name.right { left: 638px; }
  .frame { padding: 6px; }
  .frame .photo { width: 100%; height: 100%; }
  .kid { top: 329px; width: 167px; height: 221px; }
  .kid.left { left: 108px; }
  .kid.right { left: 644px; }
  .headshot { top: 180px; width: 141px; height: 493px; }
  .headshot.her { left: 308px; }
  .headshot.him { left: 470px; }
  .kid .photo { background: radial-gradient(ellipse at 50% 45%, var(--skin) 0 38%, var(--photo-light) 62%); }
  .kid.right .photo { background: radial-gradient(ellipse at 50% 42%, var(--skin) 0 38%, #b98a6a 70%, #8c6a55 100%); }
  .headshot.her .photo { background: linear-gradient(180deg, var(--photo-light) 0 10%, #d7b98b 22%, var(--skin) 34%, #5aa3b8 55%, #4a8fa6 100%); }
  .headshot.him .photo { background: linear-gradient(180deg, var(--photo-light) 0 12%, #3a2a20 20%, var(--skin-deep) 32%, #4a2c1e 50%, #3a2218 100%); }
  .caption {
    position: absolute; top: 566px; width: 200px;
    text-align: center; font-size: 30px; line-height: 41px; letter-spacing: 1px;
  }
  .caption.left { left: 92px; }
  .caption.right { left: 651px; }
  .caption .accent { color: var(--sky); }
  .title {
    left: 309px; top: 753px; width: 305px; height: 305px;
    display: flex; flex-direction: column; justify-content: center; align-items: center;
    font-size: 58px; line-height: 80px; letter-spacing: 2px; padding-top: 10px;
  }
  .tagline {
    position: absolute; left: 0; width: 100%; top: 1078px;
    text-align: center; font-size: 32px; letter-spacing: 2px; font-weight: 400;
  }
</style>
</head>
<body>
<main class="poster">
  <svg class="connectors" width="927" height="1200" viewBox="0 0 927 1200" aria-hidden="true">
    <g fill="none" stroke="#ffffff" stroke-width="2">
      <polyline points="309,130 192,130 192,224"/>
      <polyline points="611,130 727,130 727,224"/>
      <line x1="379" y1="673" x2="379" y2="753"/>
      <line x1="542" y1="673" x2="542" y2="753"/>
    </g>
  </svg>

  <div class="box heading">PERFORMERS</div>
  <div class="box performer-name left">Ray Dunsworth</div>
  <div class="box performer-name right">Linda Pruett</div>

  <div class="box frame kid left"><div class="photo" role="img" aria-label="Photo of a crying baby"></div></div>
  <div class="box frame headshot her"><div class="photo" role="img" aria-label="Headshot of performer Linda Pruett"></div></div>
  <div class="box frame headshot him"><div class="photo" role="img" aria-label="Headshot of performer Ray Dunsworth"></div></div>
  <div class="box frame kid right"><div class="photo" role="img" aria-label="Photo of a grinning baby"></div></div>

  <p class="caption left">Oh! No,<br>Not<br>Again<br>With<br>That<br><span class="accent">Babysitter!</span></p>
  <p class="caption right">Just<br>Invited<br>my<br>GIRL<br>FRIEND<br><span class="accent">Tonight!</span></p>

  <h1 class="box title"><span>Cousins</span><span>Weekend</span><span>Away!</span></h1>
  <p class="tagline">Joyfully Always Giggling.</p>
</main>
</body>
</html>
```